Senior sex novelty store providing a private method for acquiring the products and knowledge

Our business supplies novelty sex products and services, specializing in the 50+ demographic. Products include sex products for individuals and couples. Services include webinars and teleseminars that address various sex and relationship issues. We are dedicated to providing discreet delivery of products and knowledge to people over 50 entering a new phase of life, facing new challenges. Our entire process from site through shipping is kept private to allow our customers the freedom to shop and learn in the privacy of their own home.

Target Market(s)

Seniors over 50 years old

Industry/Entity Type

Store

Number of Pages Required

1 page

Font styles to use
Serif

Requirements
Must have
• place for business description with a private look
Should not have
• anything sleazy

```html
<!DOCTYPE html>
<html lang="en">
<head>
<meta charset="utf-8">
<title>Larkvale Website Sample</title>
<link rel="stylesheet" href="https://fonts.googleapis.com/css2?family=Source+Sans+3:ital,wght@0,400;1,400&family=Dancing+Script:wght@700&display=swap">
<style>
  :root {
    --navy: #34495f;
    --sky: #40a1cf;
    --coral: #f17d71;
    --coral-deep: #e5625c;
    --ring: #b5524c;
    --white: #ffffff;
    --dot: #9c9c9c;
    --dot-soft: #c9827b;
    --sans: "Source Sans 3", "Myriad Pro", sans-serif;
    --script: "Dancing Script", cursive;
  }
  * { margin: 0; padding: 0; box-sizing: border-box; }
  html, body { width: 898px; height: 1200px; overflow: hidden; }
  body { position: relative; font-family: var(--sans); color: var(--white); background: var(--coral); }

  .section { position: absolute; left: 0; width: 898px; }
  .hero { top: 0; height: 596px; background: var(--navy); }
  .products { top: 596px; height: 604px; background: var(--coral); }

  .brand { position: absolute; left: 57px; font-family: var(--sans); font-size: 34px; font-weight: 400; color: var(--white); line-height: 1; transform: translateY(-50%); }
  .hero .brand { top: 55px; }
  .products .brand { top: 56px; }

  .nav { position: absolute; right: 0; top: 0; display: flex; font-size: 13px; text-transform: uppercase; }
  .nav-item { display: flex; align-items: center; justify-content: center; height: 74px; padding: 0 16px; min-width: 64px; }
  .hero .nav-item { height: 74px; }
  .products .nav-item { height: 80px; }
  .nav-item.is-active { width: 95px; }
  .hero .nav-item.is-active { background: var(--sky); }
  .products .nav-item.is-active { background: var(--coral-deep); }
  .nav-item.last { padding-right: 57px; }

  .hero-text { position: absolute; top: 236px; left: 0; width: 100%; text-align: center; font-size: 26px; line-height: 35px; }

  .dots { position: absolute; left: 0; width: 100%; display: flex; justify-content: center; gap: 9px; }
  .dot { width: 15px; height: 15px; border-radius: 50%; background: var(--dot); }
  .dot.is-current { background: var(--white); }
  .hero .dots { top: 452px; }
  .products .dots { top: 543px; }

  .social { position: absolute; top: 486px; left: 0; width: 100%; display: flex; justify-content: center; gap: 10px; }
  .social-link { width: 32px; height: 32px; border-radius: 50%; border: 1.5px solid var(--white); }

  .pointer { position: absolute; top: 0; left: 387px; }

  .products-title { position: absolute; top: 138px; left: 0; width: 100%; text-align: center; font-size: 28px; text-transform: uppercase; line-height: 1; }
  .products-offer { position: absolute; top: 176px; left: 0; width: 100%; text-align: center; font-family: var(--script); font-size: 23px; line-height: 1; }

  .product { position: absolute; top: 247px; width: 152px; height: 152px; border-radius: 50%; border: 3px solid var(--ring); box-shadow: 6px 8px 8px rgba(120, 40, 35, 0.45); }
  .product-pump { left: 152px; background: radial-gradient(circle at 45% 55%, #f2b8cf 0%, #f7eef2 60%, #ffffff 100%); }
  .product-glass { left: 364px; background: radial-gradient(circle at 50% 50%, #3a3a3a 0%, #0b0b0b 70%); }
  .product-wand { left: 582px; background: linear-gradient(90deg, #ffffff 0%, #ffffff 38%, #7a3fb4 45%, #8b4fc4 55%, #ffffff 62%, #ffffff 100%); }

  .order { position: absolute; top: 452px; left: 0; width: 100%; text-align: center; font-size: 28px; font-style: italic; text-transform: uppercase; letter-spacing: -0.5px; }
  .order span { text-transform: none; }
</style>
</head>
<body>
  <section class="section hero">
    <div class="brand">Larkvale Website Sample</div>
    <nav class="nav">
      <div class="nav-item is-active">Home</div>
      <div class="nav-item">Products</div>
      <div class="nav-item">About</div>
      <div class="nav-item last">Contacts</div>
    </nav>
    <p class="hero-text">Our business supplies novelty sex products<br>and services, specializing in the 50+ demographic</p>
    <div class="dots">
      <span class="dot is-current"></span><span class="dot"></span><span class="dot"></span><span class="dot"></span>
    </div>
    <div class="social">
      <span class="social-link"></span><span class="social-link"></span><span class="social-link"></span><span class="social-link"></span>
    </div>
  </section>

  <section class="section products">
    <svg class="pointer" width="115" height="38" viewBox="0 0 115 38" aria-hidden="true">
      <polygon points="0,0 115,0 57.5,38" fill="var(--navy)"/>
    </svg>
    <div class="brand">Larkvale Website Sample</div>
    <nav class="nav">
      <div class="nav-item">Home</div>
      <div class="nav-item is-active">Products</div>
      <div class="nav-item">About</div>
      <div class="nav-item last">Contacts</div>
    </nav>
    <h2 class="products-title">Our Products &amp; Services</h2>
    <p class="products-offer">Discount 20% on all items</p>
    <div class="product product-pump" role="img" aria-label="Product photo: pink vacuum pump set"></div>
    <div class="product product-glass" role="img" aria-label="Product photo: clear glass toy on black"></div>
    <div class="product product-wand" role="img" aria-label="Product photo: purple vibrator"></div>
    <p class="order">Order Now!!!</p>
    <div class="dots">
      <span class="dot"></span><span class="dot is-current"></span><span class="dot"></span><span class="dot"></span>
    </div>
  </section>
</body>
</html>
```